Orbin Vale Systems

Our company is about IT hardwares and IT solutions. IT hardware such as PC, RAMS, storage and servers. IT solutions such as project management, BA. We are also selling new technology too.

Target Market(s)

Consumer, Small to Medium Business, Corporate

Requirements
Must have
• The business card must have the following:
• Name:
• Title:
• Contact Number:
• Email address:
• Website:
• Color: Must match the logo color upgrade

```html
<!DOCTYPE html>
<html lang="en">
<head>
<meta charset="utf-8">
<title>Orbin Vale Systems — Business Card</title>
<link href="https://fonts.googleapis.com/css2?family=Lato:wght@400;700;900&display=swap" rel="stylesheet">
<style>
  :root {
    --stage: #161616;
    --card-dark: #232323;
    --card-dark-deep: #1c1c1c;
    --paper: #ffffff;
    --accent: #e09a35;
    --accent-deep: #c87a22;
    --ink-light: #f2f2f2;
    --ink-dark: #3a3a3a;
  }
  * { box-sizing: border-box; margin: 0; padding: 0; }
  html, body {
    width: 1200px; height: 912px; overflow: hidden;
    background: var(--stage);
    font-family: "Lato", Arial, sans-serif;
  }
  .stage {
    position: relative; width: 1200px; height: 912px;
  }
  .card {
    position: absolute; left: 250px; width: 700px; height: 400px;
    overflow: hidden; border-radius: 4px;
    box-shadow: 0 14px 30px rgba(0,0,0,.55);
  }
  /* Back side */
  .card-back {
    top: 40px;
    background: linear-gradient(135deg, var(--card-dark) 0%, var(--card-dark-deep) 100%);
  }
  .brand {
    position: absolute; display: flex; align-items: center; gap: 14px;
    font-weight: 900; letter-spacing: 1px; text-transform: uppercase;
  }
  .brand-mark {
    border-radius: 50%; background: var(--accent); flex: none;
  }
  .card-back .brand {
    left: 0; right: 0; top: 150px; justify-content: center;
    font-size: 46px; color: var(--ink-light);
  }
  .card-back .brand-mark { width: 34px; height: 34px; }
  .card-back .web {
    position: absolute; left: 0; right: 0; bottom: 52px; text-align: center;
    color: var(--ink-light); font-size: 17px; letter-spacing: .5px;
  }
  /* Front side */
  .card-front { top: 470px; background: var(--card-dark); }
  .card-front svg.backdrop { position: absolute; inset: 0; }
  .card-front .brand {
    right: 44px; top: 84px; font-size: 34px; color: var(--ink-dark);
  }
  .card-front .brand-mark { width: 26px; height: 26px; }
  .person { position: absolute; left: 44px; top: 236px; }
  .person-name { color: var(--accent); font-weight: 700; font-size: 28px; }
  .person-title { color: var(--ink-light); font-size: 16px; margin-top: 2px; }
  .contacts { list-style: none; margin-top: 12px; }
  .contacts li {
    display: flex; align-items: center; gap: 12px;
    color: var(--ink-light); font-size: 15.5px; line-height: 22px;
  }
  .contacts svg { width: 14px; height: 14px; fill: var(--accent); flex: none; }
  .address {
    position: absolute; right: 44px; bottom: 150px; text-align: right;
    color: var(--ink-light); font-size: 16px; line-height: 22px;
  }
</style>
</head>
<body>
<main class="stage">

  <section class="card card-back" aria-label="Card back">
    <div class="brand"><span class="brand-mark"></span>Orbin Vale Systems</div>
    <p class="web">www.orbinvale.com</p>
  </section>

  <section class="card card-front" aria-label="Card front">
    <svg class="backdrop" viewBox="0 0 700 400" width="700" height="400" aria-hidden="true">
      <path d="M0 0 H700 V150 C560 235 360 255 170 225 C100 214 45 198 0 182 Z" fill="var(--paper)"/>
      <path d="M20 190 C120 225 260 240 400 222 C300 232 160 226 20 198 Z" fill="var(--accent)"/>
    </svg>

    <div class="brand"><span class="brand-mark"></span>Orbin Vale Systems</div>

    <div class="person">
      <h1 class="person-name">Dana Whitlock</h1>
      <p class="person-title">Manager</p>
      <ul class="contacts">
        <li><svg viewBox="0 0 16 16"><path d="M3 1h3l1.5 4-2 1.5a9 9 0 0 0 4 4L11 8.5l4 1.5v3a2 2 0 0 1-2 2A12 12 0 0 1 1 3a2 2 0 0 1 2-2z"/></svg>555 010 4800</li>
        <li><svg viewBox="0 0 16 16"><path d="M4 1h8v4H4zM1 6h14v6h-3v3H4v-3H1zM5 10v4h6v-4z"/></svg>555 010 4801</li>
        <li><svg viewBox="0 0 16 16"><path d="M1 3h14v10H1zM2 4l6 5 6-5v1L8 10 2 5z" fill-rule="evenodd"/></svg>info@orbinvale.com</li>
        <li><svg viewBox="0 0 16 16"><path d="M8 1a7 7 0 1 0 0 14A7 7 0 0 0 8 1zm0 1.5c1 1 1.6 2.6 1.8 4.5H6.2C6.4 5.1 7 3.5 8 2.5zM6.2 9h3.6c-.2 1.9-.8 3.5-1.8 4.5-1-1-1.6-2.6-1.8-4.5zM2.6 7a5.5 5.5 0 0 1 2.4-3.8A9 9 0 0 0 4.7 7zm0 2h2.1a9 9 0 0 0 .3 3.8A5.5 5.5 0 0 1 2.6 9zm8.7 0h2.1a5.5 5.5 0 0 1-2.4 3.8 9 9 0 0 0 .3-3.8zm0-2a9 9 0 0 0-.3-3.8A5.5 5.5 0 0 1 13.4 7z"/></svg>www.orbinvale.com</li>
      </ul>
    </div>

    <address class="address" style="font-style:normal">48 Larch Row<br>Fairview, TX 75069</address>
  </section>

</main>
</body>
</html>
```